Chimney Service company needs new business card design

We need a updated business card with our new logo added. We provide a full range of chimney services throughout Vermont and New Hampshire. The business card will be one sided and color. Attached is our current business card another document showing all the information we would like on the card.
We dont like a lot of flashy colors.... here is a link to our website to get an idea of our branding www.flueguardianvt.example

Target Market(s)

homeowners

Industry/Entity Type

Business

Contact Information for Business Card

See attached sheet for content.

Font styles to use
Serif
Sans Serif

Requirements
Must have
• all information provided on separate sheet
Should not have
• Additional information that may clogg up design

```html
<!DOCTYPE html>
<html lang="en">
<head>
<meta charset="utf-8">
<title>Flue Guardian business card</title>
<link rel="stylesheet" href="https://fonts.googleapis.com/css2?family=Crimson+Pro:wght@400;500;600&display=swap">
<style>
  :root {
    --backdrop: #1d1a19;
    --card: #3a3a3c;
    --band: #c8c8c8;
    --ink-light: #ececec;
    --ink-dark: #2b2b2d;
    --rule: #bdbdbd;
  }
  * { margin: 0; padding: 0; box-sizing: border-box; }
  html, body { width: 1200px; height: 716px; overflow: hidden; background: var(--backdrop); }
  body { font-family: "Crimson Pro", "Times New Roman", serif; }
  .card {
    position: absolute; left: 80px; top: 61px; width: 1040px; height: 594px;
    background: var(--card); color: var(--ink-light); overflow: hidden;
  }
  .card-shapes { position: absolute; inset: 0; }
  .brand { position: absolute; left: 44px; top: 38px; display: flex; align-items: center; gap: 16px; }
  .brand-mark { width: 50px; height: 50px; background: var(--ink-light); }
  .brand-name { font-size: 38px; font-weight: 500; letter-spacing: 1px; text-transform: uppercase; line-height: 1; }
  .brand-since { position: absolute; left: 220px; top: 98px; font-size: 16px; letter-spacing: 3px; }
  .tagline { position: absolute; left: 48px; top: 124px; font-size: 22px; color: var(--ink-dark); }
  .contact { position: absolute; left: 66px; top: 186px; list-style: none; font-size: 19px; line-height: 30px; }
  .contact li { display: flex; align-items: center; gap: 12px; }
  .contact svg { width: 16px; height: 16px; }
  .assurances { position: absolute; left: 66px; top: 318px; font-size: 21px; line-height: 28px; }
  .service { position: absolute; font-size: 22px; color: var(--ink-dark); line-height: 30px; white-space: nowrap; }
</style>
</head>
<body>
<div class="card">
  <svg class="card-shapes" width="1040" height="594" viewBox="0 0 1040 594">
    <line x1="212" y1="94" x2="470" y2="94" stroke="var(--ink-light)" stroke-width="2"/>
    <rect x="0" y="122" width="620" height="32" fill="var(--band)"/>
    <line x1="40" y1="392" x2="560" y2="392" stroke="var(--rule)" stroke-width="1.5"/>
    <polygon points="0,500 340,500 328,530 0,530" fill="var(--band)"/>
    <polygon points="352,500 730,500 718,530 340,530" fill="var(--band)"/>
    <polygon points="742,500 1040,500 1040,530 730,530" fill="var(--band)"/>
    <polygon points="0,536 430,536 418,566 0,566" fill="var(--band)"/>
    <polygon points="442,536 1040,536 1040,566 430,566" fill="var(--band)"/>
  </svg>

  <div class="brand">
    <span class="brand-mark"></span>
    <span class="brand-name">Flue Guardian</span>
  </div>
  <div class="brand-since">INC 1989</div>
  <p class="tagline">Serving VT and New Hampshire since 1989</p>

  <ul class="contact">
    <li><svg viewBox="0 0 16 16"><path d="M4 1l3 3-2 2c1 2 3 4 5 5l2-2 3 3-2 3C7 15 1 9 1 3z" fill="var(--ink-light)"/></svg>802-555-0147</li>
    <li><svg viewBox="0 0 16 16"><rect x="1" y="3" width="14" height="10" fill="none" stroke="var(--ink-light)" stroke-width="1.3"/><path d="M1 3l7 6 7-6" fill="none" stroke="var(--ink-light)" stroke-width="1.3"/></svg>info@flueguardianvt.example</li>
    <li><svg viewBox="0 0 16 16"><circle cx="8" cy="8" r="6.5" fill="none" stroke="var(--ink-light)" stroke-width="1.3"/><ellipse cx="8" cy="8" rx="3" ry="6.5" fill="none" stroke="var(--ink-light)" stroke-width="1"/><line x1="1.5" y1="8" x2="14.5" y2="8" stroke="var(--ink-light)" stroke-width="1"/></svg>www.flueguardianvt.example</li>
  </ul>

  <div class="assurances">
    <p>Fully Insured – Free Estimates</p>
    <p>Family owned and operated</p>
  </div>

  <span class="service" style="left:14px; top:500px;">Full Masonry Services</span>
  <span class="service" style="left:370px; top:500px;">Historic chimney restoration</span>
  <span class="service" style="right:18px; top:500px;">Stainless steel liners</span>
  <span class="service" style="left:14px; top:536px;">New Chimney installations</span>
  <span class="service" style="right:18px; top:536px;">Fully Certified Chimney sweeps</span>
</div>
</body>
</html>
```